Business Card Design

We need a sharp, bold, crisp logo and business card that helps express confidence in what we do. The logo can either have the name of the company in it, or somehow use the first initials of each of the two words in the name, or it doesn't have to have any text in the logo at all.

Target Market(s)

Upper management of small to midsize companies (Presidents, CEOs, Executive Directors, Executive Managers, etc.)

Industry/Entity Type

Business

Contact Information for Business Card

Name of company: Brightpath Advisors, LLC;
My name and title: Dana Melkovic - President;
My phone number: 555-318-2070;
My email address: dana@brightpathadvisors.example;
The website: www.brightpathadvisors.example

Requirements
Must have
• Bullets of what we do: - Quality Systems Development & Implementation, - Process Improvement Services, - Problem Solving Services, - Quality System Auditing, - Customized In-House Training, - MS TeamVault Site Development
Nice to have
• What we do: We specialize in Quality Systems & Process Improvement Consulting Services. We help non-automotive industries and automotive suppliers to achieve and exceed their Quality and Efficiency goals by leveraging and applying a tremendous amount of excellent automotive industry quality systems experience into your organization’s processes.

```html
<!DOCTYPE html>
<html lang="en">
<head>
<meta charset="utf-8">
<title>Brightpath Advisors, LLC — Business Card</title>
<link rel="stylesheet" href="https://fonts.googleapis.com/css2?family=Oswald:wght@300;400&display=swap">
<style>
  :root {
    --card-bg: #1f2323;
    --accent-red: #8e0f12;
    --name-white: #ffffff;
    --body-text: #d9dddd;
  }
  html, body {
    margin: 0;
    padding: 0;
    width: 1200px;
    height: 702px;
    overflow: hidden;
    background: var(--card-bg);
  }
  .card {
    position: relative;
    width: 1200px;
    height: 702px;
    background: var(--card-bg);
    font-family: "Oswald", "Arial Narrow", sans-serif;
  }
  .brand {
    position: absolute;
    left: 62px;
    top: 0;
    width: 440px;
    height: 702px;
    display: flex;
    flex-direction: column;
    justify-content: center;
    align-items: flex-start;
  }
  .brand-square {
    width: 72px;
    height: 72px;
    background: var(--accent-red);
    margin-bottom: 34px;
  }
  .brand-name {
    margin: 0;
    color: var(--name-white);
    font-weight: 300;
    text-transform: uppercase;
    line-height: 1.08;
  }
  .brand-name .line-main {
    display: block;
    font-size: 74px;
    letter-spacing: 4px;
  }
  .brand-name .line-sub {
    display: block;
    font-size: 46px;
    letter-spacing: 7px;
    margin-top: 6px;
  }
  .divider {
    position: absolute;
    left: 564px;
    top: 72px;
    width: 3px;
    height: 552px;
    background: var(--accent-red);
  }
  .about {
    position: absolute;
    left: 606px;
    top: 68px;
    width: 520px;
    margin: 0;
    color: var(--body-text);
    font-weight: 300;
    font-size: 35.5px;
    line-height: 55.3px;
    letter-spacing: 0.2px;
  }
</style>
</head>
<body>
  <main class="card">
    <section class="brand" aria-label="Brightpath Advisors, LLC">
      <div class="brand-square"></div>
      <h1 class="brand-name">
        <span class="line-main">Brightpath</span>
        <span class="line-sub">Advisors, LLC</span>
      </h1>
    </section>
    <div class="divider"></div>
    <p class="about">We specialize in Quality Systems &amp; Process Improvement Consulting Services. We help non-automotive industries and automotive suppliers to achieve and exceed their Quality and Efficiency goals by leveraging and applying a tremendous amount of excellent automotive industry quality systems experience into your organization’s processes.</p>
  </main>
</body>
</html>
```